A4 Childcare Spring Special Flyer

Ferngate Skills Academy is a registered training organisation (RTO) Toid No. 47318, based in Blackburn, Victoria. We are a market leader in Professional development courses both accredited and non accredited, in order for you to maintain currency in your profession.

We need a flyer for a childcare specific spring special. The special is to offer a $50 LUMBO gift card and 50% of your second training session. Conditions apply*

The training sessions available are the NEW childcare specific course: HLTAID004 Provide an emergency first aid response in an education and care setting and HLTAID003 Provide First Aid, HLTAID001 Provide Cardiopulmonary Resuscitation (CPR), 22024VIC Course in emergency management of asthma in the workplace
and 22099VIC Course in First Aid Management of Anaphylaxis.
We provide a flexible, cost effective and reliable service.
We have training locations available in Blackburn, Preston, Narre Warren and Mornington and can also provide onsite training.

We can also provide education and QERSOB regulation consultation to the childcare provider.

Must use company logo, include phone number: (03) 5550 1274, website: www.ferngateskillsacademy.com.au, email: maraflint@ferngateskillsacademy.com.au

(Note that a letter with more detail will be attached with this flyer, therefore, with that in mind; use that information as desired).

The final product should be as childcare like as possible whilst also keeping our company colors (same as logo). We would also like for this flyer to stand out and be appealing to the recipient as this flyer is to gain potential clients, with emphasis on the HLTAID004 Course
Updates

Just need to update the qualifications: In the design brief I mentioned that the course; HLTAID001 Provide CPR and Asthma & Anaphyalxis.. Can this please be changed to HLTAID001 Provide Cardiopulmonary Resuscitation (CPR) And 22024VIC Course in emergency management of asthma in the workplace And 22099VIC Course in First Aid Management of Anaphylaxis (They are all singular courses) Apoligies!

Target Market(s)

Childcare centres, Out of school hours providers, pre-schools

Industry/Entity Type

Childcare

Font styles to use
Decorative

Colors
ffcf3e
f37123
faa54b

Requirements
Must have
• Company Logo
phone number
website
email
Registered Training Organisation
TOID: 47318

```html
<!DOCTYPE html>
<html lang="en">
<head>
<meta charset="utf-8">
<title>Ferngate Skills Academy – Childcare Spring Special</title>
<link rel="stylesheet" href="https://fonts.googleapis.com/css2?family=Cinzel:wght@700&family=Questrial&display=swap">
<style>
  :root{
    --yellow:#ffcf3e;
    --orange:#f37123;
    --light-orange:#faa54b;
    --deep-orange:#e4571b;
    --paper:#f6f6f6;
    --ink:#1d1d1d;
    --grey:#5a5a5a;
    --stage:#e8e8e8;
    --card-blue:#1f3a8a;
  }
  *{margin:0;padding:0;box-sizing:border-box}
  html,body{width:923px;height:1200px;overflow:hidden;background:var(--stage)}
  .flyer{
    position:absolute;left:50px;top:24px;width:658px;height:922px;
    transform:scale(1.25);transform-origin:0 0;
    background:linear-gradient(135deg,#ffffff 0%,var(--paper) 60%,#ececec 100%);
    overflow:hidden;font-family:"Questrial",sans-serif;color:var(--ink);
  }
  .mosaic{position:absolute;inset:0}
  .photo{position:absolute}
  .brand{
    position:absolute;left:212px;top:130px;width:160px;text-align:center;
    font-family:"Questrial",sans-serif;color:var(--grey);font-size:22px;line-height:1.1;
  }
  .brand-dot{width:64px;height:64px;border-radius:50%;background:var(--orange);margin:0 auto 14px}
  .rto{
    position:absolute;left:488px;top:38px;transform:rotate(-12deg);
    font-family:"Cinzel",serif;font-weight:700;color:#fff;font-size:15px;line-height:1.35;text-align:center;
  }
  .toid{position:absolute;right:10px;top:126px;font-size:9px;color:var(--ink)}
  .headline{
    position:absolute;left:368px;top:262px;transform:rotate(-3deg);
    font-family:"Cinzel",serif;font-weight:700;color:#fff;font-size:19px;line-height:1.3;text-align:center;width:230px;
  }
  .list{position:absolute;left:333px;list-style:none;width:300px;font-size:12.5px;line-height:1.3}
  .list li{position:relative;padding-left:12px;margin-bottom:13px}
  .list li::before{content:"";position:absolute;left:0;top:4px;width:8px;height:8px;background:var(--light-orange)}
  .list li.alt::before{background:var(--orange)}
  .list li.hot::before{background:var(--deep-orange)}
  .courses{top:353px}
  .courses .lead{font-weight:700;font-family:"Questrial",sans-serif;-webkit-text-stroke:.4px var(--ink)}
  .benefits{top:608px}
  .benefits li:first-child::before{background:var(--yellow)}
  .divider{position:absolute;left:408px;top:585px;width:160px;height:2px;background:var(--orange);border-radius:2px}
  .contact{position:absolute;left:14px;top:800px;list-style:none;font-size:11.5px;color:#fff}
  .contact li{display:flex;align-items:center;height:21px}
  .contact svg{width:15px;height:15px;margin-right:9px;flex:none}
  .offer-label{
    position:absolute;left:415px;top:826px;transform:rotate(-2deg);
    font-family:"Cinzel",serif;font-weight:700;color:#fff;font-size:12px;
  }
  .discount{
    position:absolute;left:300px;top:860px;width:170px;transform:rotate(5deg);
    font-family:"Cinzel",serif;font-weight:700;color:#fff;font-size:12.5px;line-height:1.15;text-align:center;
  }
  .gift-card{position:absolute;left:534px;top:794px;width:94px;height:62px;border:3px solid var(--yellow);border-radius:3px;
    background:linear-gradient(160deg,#2d4fa8,var(--card-blue))}
  .gift-value{position:absolute;left:590px;top:856px;font-family:"Cinzel",serif;font-weight:700;font-size:24px;color:var(--yellow);
    -webkit-text-stroke:.6px #3a2a10}
</style>
</head>
<body>
<main class="flyer">
  <svg class="mosaic" viewBox="0 0 658 922" width="658" height="922" aria-hidden="true">
    <!-- top left blocks -->
    <polygon points="0,0 200,0 198,88 0,104" fill="var(--yellow)"/>
    <polygon points="0,112 105,104 108,282 0,290" fill="var(--light-orange)"/>
    <polygon points="113,100 196,94 194,200 112,204" fill="var(--orange)"/>
    <polygon points="110,210 194,206 192,284 108,286" fill="var(--light-orange)"/>
    <polygon points="0,296 170,290 170,300 0,300" fill="var(--orange)"/>
    <!-- logo panel -->
    <polygon points="207,0 384,0 338,256 203,256" fill="#fbfbfb" stroke="#8a8a8a" stroke-width="1.5"/>
    <!-- top right blocks -->
    <polygon points="392,0 478,0 478,150 362,162" fill="var(--yellow)"/>
    <polygon points="484,0 658,0 658,140 484,150" fill="var(--light-orange)"/>
    <polygon points="484,156 658,148 658,250 482,262" fill="var(--yellow)"/>
    <polygon points="410,170 472,166 472,228 408,232" fill="var(--light-orange)"/>
    <polygon points="360,170 402,168 400,234 350,236" fill="var(--orange)"/>
    <!-- headline banner -->
    <polygon points="350,244 476,238 476,268 658,258 658,322 336,330" fill="var(--orange)"/>
    <polygon points="315,270 336,268 330,330 312,332" fill="var(--orange)"/>
    <!-- photo frames -->
    <rect x="0" y="296" width="170" height="130" fill="var(--yellow)"/>
    <polygon points="176,258 314,256 310,456 176,460" fill="var(--orange)"/>
    <rect x="0" y="432" width="164" height="112" fill="var(--orange)"/>
    <polygon points="168,460 298,456 296,552 168,552" fill="var(--yellow)"/>
    <polygon points="0,556 268,552 262,738 0,742" fill="var(--orange)"/>
    <polygon points="270,556 284,556 278,640 264,640" fill="var(--light-orange)"/>
    <!-- lower left blocks -->
    <polygon points="34,744 72,742 70,782 32,782" fill="var(--yellow)"/>
    <polygon points="78,742 132,740 130,782 76,782" fill="var(--light-orange)"/>
    <polygon points="138,740 198,738 196,780 136,782" fill="var(--yellow)"/>
    <polygon points="206,738 262,736 260,772 204,774" fill="var(--orange)"/>
    <polygon points="0,744 28,744 26,790 0,790" fill="var(--light-orange)"/>
    <!-- contact band -->
    <polygon points="0,792 258,788 252,866 0,870" fill="var(--light-orange)"/>
    <!-- bottom strip -->
    <polygon points="0,878 120,874 118,922 0,922" fill="var(--deep-orange)"/>
    <polygon points="126,880 210,876 210,922 124,922" fill="var(--orange)"/>
    <polygon points="216,884 280,882 282,922 216,922" fill="var(--light-orange)"/>
    <!-- special offer -->
    <polygon points="296,778 410,770 412,816 528,808 540,922 286,922" fill="var(--orange)"/>
    <polygon points="356,800 378,800 378,820 392,820 367,846 342,820 356,820" fill="#fff"/>
    <polygon points="536,872 658,866 658,922 544,922" fill="var(--deep-orange)"/>
    <polygon points="634,742 658,740 658,800 634,802" fill="var(--yellow)"/>
    <polygon points="634,806 658,804 658,860 636,862" fill="var(--light-orange)"/>
  </svg>

  <div class="photo" role="img" aria-label="Photo of cheerful preschool children raising their arms in a play room" style="left:6px;top:302px;width:158px;height:118px;background:linear-gradient(135deg,#d9745a,#6aa6c9 60%,#e8b25a)"></div>
  <div class="photo" role="img" aria-label="Photo of a trainer bandaging a young girl's knee" style="left:184px;top:266px;width:120px;height:184px;background:linear-gradient(160deg,#a7794f,#d8b79a 50%,#8c6a4b)"></div>
  <div class="photo" role="img" aria-label="Photo of gloved hands practising CPR on an infant manikin" style="left:6px;top:438px;width:152px;height:100px;background:linear-gradient(135deg,#3a2b27,#c9a99a 55%,#4d5fb0)"></div>
  <div class="photo" role="img" aria-label="Photo of a toddler using an asthma inhaler" style="left:174px;top:466px;width:118px;height:80px;background:linear-gradient(135deg,#8a9aa4,#d9c2a6 60%,#6e7b86)"></div>
  <div class="photo" role="img" aria-label="Photo of two educators with a group of children at a classroom table" style="left:10px;top:562px;width:244px;height:170px;background:linear-gradient(180deg,#e3e3de,#c9a47f 55%,#b07a4b)"></div>

  <div class="brand"><div class="brand-dot"></div>Ferngate Skills Academy</div>

  <div class="rto">Registered<br>Training<br>Organisation</div>
  <div class="toid">TOID 47318</div>

  <h1 class="headline">New Childcare<br>Specific Courses</h1>

  <ul class="list courses">
    <li class="lead hot">HLTAID004 Provide an emergency first aid response in an education and care setting</li>
    <li>HLTAID003 Provide First Aid</li>
    <li>HLTAID001 Provide Cardiopulmonary Resuscitation (CPR)</li>
    <li>22024VIC Course in emergency management of asthma in the workplace</li>
    <li class="alt">22099VIC Course in First Aid Management of Anaphylaxis</li>
  </ul>

  <div class="divider"></div>

  <ul class="list benefits">
    <li>Flexible, cost effective, reliable service</li>
    <li class="alt">Training locations available in Blackburn, Preston, Narre Warren and Mornington and can also provide onsite training</li>
    <li class="hot">Provide education and QERSOB regulation consultation to the childcare provider</li>
  </ul>

  <ul class="contact">
    <li><svg viewBox="0 0 16 16"><circle cx="8" cy="8" r="8" fill="#6b6b6b"/><path d="M4 5.5h8v5H4z M4 5.5l4 3 4-3" fill="none" stroke="#fff" stroke-width="1"/></svg>maraflint@ferngateskillsacademy.com.au</li>
    <li><svg viewBox="0 0 16 16"><circle cx="8" cy="8" r="8" fill="#6b6b6b"/><rect x="5.5" y="4" width="5" height="8" rx="2.5" fill="none" stroke="#fff" stroke-width="1"/><line x1="8" y1="5" x2="8" y2="7" stroke="#fff"/></svg>www.ferngateskillsacademy.com.au</li>
    <li><svg viewBox="0 0 16 16"><rect width="16" height="16" rx="3" fill="#6b6b6b"/><path d="M5 3.5l2 2-1 1.2c.6 1.4 1.6 2.4 3 3l1.2-1 2 2-1.3 1.5C7.5 11.8 4.2 8.5 3.7 5z" fill="#fff"/></svg>(03) 5550 1274</li>
  </ul>

  <div class="offer-label">Special Offer</div>
  <div class="discount">50% Discount<br>of your second<br>training session</div>

  <div class="gift-card" role="img" aria-label="LUMBO gift card"></div>
  <div class="gift-value">$50</div>
</main>
</body>
</html>
```